Business cards and Stationary | Lumora Music Events

Hello! We need business cards and stationery for a new small business in the music industry. "Lumora is a high-end music agency which provides an unparalleled level of talent and personalized service to the realm entertainment, corporate events, and luxury weddings. Here is where the classical meets the contemporary and we can bring your vision to life.Keeping a steady finger on the pulse of current trends and consistently raising the bar for industry standards, Lumora continues to rise to the forefront of the music industry, providing the utmost professional, high-end, elegant, and engaging entertainment in Australia and World-Wide."

Target Market(s)

Class A. high profile corporate business.

Industry/Entity Type

Entertainment

Contact Information for Business Card

Lumora Music Events

Clare Yoshinaga
Director | Violinist

Level 7, 41 Caddow Lane
Sydney, 2000

Website: www.lumoramusicevents-demo.net
Phone number: 0455 318 602
Email: clare@lumoramusicevents-demo.net

Font styles to use
Serif
Sans Serif
Script

Colors
feeeee
0355a3
f59296
ffffff

Requirements
Nice to have
• Clean and sophisticated would be perfect.
• If there is a way to include the Instagram without being tacky, that would be awesome
• @lumoramusicevents
• Our website and logo have the following fonts:
• The primary logo is inspired and based on a font called BillionScript but the B is completely hand drawn and the rest is customised a bit to work together cohesively
• Monserrat Light - Is the Music part of the logo and as headers in the site
• Open Sans 300 and 400 (Light or Regular) is used mostly as the body text in the site
• If you want to access the website:
• www.lumoramusicevents-demo.net
• username: client
• password: preview

```html
<!DOCTYPE html>
<html lang="en">
<head>
<meta charset="utf-8">
<title>Lumora Music Events – Stationery</title>
<link href="https://fonts.googleapis.com/css2?family=Montserrat:wght@300;400&family=Open+Sans:wght@400;600;700&display=swap" rel="stylesheet">
<style>
  :root{
    --bg:#ecedef;
    --navy:#232c8a;
    --navy-light:#2f3fae;
    --blush:#fbe9ea;
    --rose:#c9948f;
    --blue-text:#1f4fa0;
    --ink:#1d1d24;
    --white:#ffffff;
  }
  *{box-sizing:border-box;margin:0;padding:0}
  html,body{width:872px;height:1200px;overflow:hidden;background:var(--bg)}
  body{position:relative;font-family:"Open Sans",Arial,sans-serif;color:var(--ink)}
  .piece{position:absolute;overflow:hidden;box-shadow:0 2px 6px rgba(0,0,0,.18)}

  .brand-name{font-family:"Montserrat",Arial,sans-serif;font-weight:300;color:var(--rose);letter-spacing:.18em;text-transform:uppercase;white-space:nowrap;display:flex;align-items:center;gap:8px}
  .brand-dot{width:13px;height:13px;border:1px solid var(--rose);border-radius:50%;flex:none}

  .contact-list{position:absolute;font-size:7px;line-height:1}
  .contact-row{display:flex;align-items:center;gap:12px;margin-bottom:7px}
  .contact-item{display:flex;align-items:center;gap:4px;white-space:nowrap}
  .icon{width:11px;height:11px;flex:none}

  .handle{display:flex;align-items:center;gap:5px;font-size:9px;white-space:nowrap}
  .handle-dot{width:11px;height:11px;border:1.2px solid currentColor;border-radius:50%}

  /* envelope */
  .envelope{left:80px;top:46px;width:538px;height:240px;background:var(--blush)}
  .envelope .photo{position:absolute;right:0;top:0;width:80px;height:208px;background:linear-gradient(90deg,rgba(251,233,234,0),#c9a39a 45%,#a8786c)}
  .envelope .brand-name{position:absolute;left:262px;top:100px;font-size:16px}
  .envelope .contact-list{left:40px;top:150px;color:#2a2a35}
  .envelope .band{position:absolute;left:0;bottom:0;width:100%;height:32px;background:var(--navy)}
  .envelope .handle{position:absolute;left:40px;top:10px;color:#c8cbe8}

  /* card front */
  .card-front{left:80px;top:295px;width:256px;height:146px;background:linear-gradient(135deg,#2a3597,var(--navy) 70%)}
  .card-front .halo{position:absolute;left:66px;top:10px;width:124px;height:124px;border-radius:50%;background:radial-gradient(circle,#2f49b8,#2a3aa4 70%,rgba(42,58,164,0))}
  .card-front .brand-name{position:absolute;left:0;width:100%;top:62px;justify-content:center;font-size:14px}

  /* card back */
  .card-back{left:365px;top:295px;width:256px;height:146px;background:var(--blush)}
  .card-back .photo{position:absolute;right:0;top:0;width:80px;height:130px;background:linear-gradient(90deg,rgba(251,233,234,0),#dcbcb4 45%,#c59d93)}
  .card-back .holder{position:absolute;left:15px;top:37px}
  .holder-name{font-size:11.5px;color:var(--blue-text)}
  .holder-name b{font-weight:700}
  .holder-role{font-size:6.5px;font-weight:600;margin-top:1px}
  .card-back .contact-list{left:15px;top:73px;font-size:5px}
  .card-back .contact-row{gap:7px;margin-bottom:4px}
  .card-back .icon{width:8px;height:8px}
  .card-back .handle{position:absolute;left:0;width:100%;justify-content:center;top:131px;font-size:6px;color:var(--rose)}
  .card-back .handle-dot{width:7px;height:7px;border-width:1px}

  /* letterhead */
  .letterhead{left:73px;top:465px;width:549px;height:704px;background:var(--white)}
  .letterhead .header-band{position:absolute;left:0;top:0;width:549px;height:61px}
  .letterhead .brand-name{position:absolute;left:34px;top:64px;font-size:17px}
  .letterhead .contact-list{right:20px;top:13px;color:var(--white);font-size:6.8px}
  .letterhead .contact-row{gap:10px;margin-bottom:6px}
  .recipient{position:absolute;left:34px;top:137px;font-size:7.3px;line-height:11px}
  .recipient-name{font-size:9.5px;font-weight:700;color:var(--blue-text)}
  .letter-date{position:absolute;right:33px;top:137px;font-size:7.3px}
  .letter-body{position:absolute;left:34px;top:222px;width:484px;font-size:7.3px;line-height:16.5px;text-align:justify}
  .letter-body p{text-indent:8px;margin-bottom:16.5px}
  .sign-off{position:absolute;left:34px;top:586px;font-size:7.3px;line-height:11px}
  .signer{margin-top:17px;font-size:9px;font-weight:700}
  .footer-band{position:absolute;left:0;top:677px;width:549px;height:19px}
  .footer-band .seg-left{position:absolute;left:0;top:0;width:65px;height:19px;background:var(--navy)}
  .footer-band .seg-right{position:absolute;left:194px;top:0;right:0;height:19px;background:var(--navy)}
  .footer-band .handle{position:absolute;left:70px;top:3px;font-size:10px;color:var(--rose)}
</style>
</head>
<body>

<svg width="0" height="0" style="position:absolute">
  <defs>
    <symbol id="i-pin" viewBox="0 0 12 12"><circle cx="6" cy="6" r="5.3" fill="none" stroke="#1f4fa0" stroke-width="1"/><path d="M6 2.8a2 2 0 0 1 2 2c0 1.5-2 4-2 4s-2-2.5-2-4a2 2 0 0 1 2-2z" fill="#1f4fa0"/></symbol>
    <symbol id="i-phone" viewBox="0 0 12 12"><circle cx="6" cy="6" r="5.3" fill="none" stroke="#1f4fa0" stroke-width="1"/><path d="M3.4 4.5h5.2v1.2l-1 .3v1.8h-3.2V6l-1-.3z" fill="#1f4fa0"/></symbol>
    <symbol id="i-mobile" viewBox="0 0 12 12"><circle cx="6" cy="6" r="5.3" fill="#1f4fa0"/><path d="M4.2 3.5l1 .1.5 1.3-.6.5a4 4 0 0 0 1.6 1.6l.5-.6 1.3.5.1 1a1 1 0 0 1-1 .6A4.8 4.8 0 0 1 3.6 4.5a1 1 0 0 1 .6-1z" fill="#fff"/></symbol>
    <symbol id="i-mail" viewBox="0 0 12 12"><circle cx="6" cy="6" r="5.3" fill="none" stroke="#1f4fa0" stroke-width="1"/><rect x="3.3" y="4.2" width="5.4" height="3.6" fill="#1f4fa0"/><path d="M3.3 4.2L6 6.2l2.7-2" fill="none" stroke="#fff" stroke-width=".6"/></symbol>
    <symbol id="i-web" viewBox="0 0 12 12"><circle cx="6" cy="6" r="5.3" fill="none" stroke="#1f4fa0" stroke-width="1"/><rect x="3.4" y="3.8" width="5.2" height="3.6" rx=".4" fill="none" stroke="#1f4fa0" stroke-width=".8"/><path d="M5 8.4h2" stroke="#1f4fa0" stroke-width=".8"/></symbol>
    <symbol id="w-pin" viewBox="0 0 12 12"><circle cx="6" cy="6" r="5.3" fill="none" stroke="#fff" stroke-width="1"/><path d="M6 2.8a2 2 0 0 1 2 2c0 1.5-2 4-2 4s-2-2.5-2-4a2 2 0 0 1 2-2z" fill="#fff"/></symbol>
    <symbol id="w-phone" viewBox="0 0 12 12"><circle cx="6" cy="6" r="5.3" fill="none" stroke="#fff" stroke-width="1"/><path d="M3.4 4.5h5.2v1.2l-1 .3v1.8h-3.2V6l-1-.3z" fill="#fff"/></symbol>
    <symbol id="w-mobile" viewBox="0 0 12 12"><circle cx="6" cy="6" r="5.3" fill="none" stroke="#fff" stroke-width="1"/><path d="M4.2 3.5l1 .1.5 1.3-.6.5a4 4 0 0 0 1.6 1.6l.5-.6 1.3.5.1 1a1 1 0 0 1-1 .6A4.8 4.8 0 0 1 3.6 4.5a1 1 0 0 1 .6-1z" fill="#fff"/></symbol>
    <symbol id="w-mail" viewBox="0 0 12 12"><circle cx="6" cy="6" r="5.3" fill="none" stroke="#fff" stroke-width="1"/><rect x="3.3" y="4.2" width="5.4" height="3.6" fill="none" stroke="#fff" stroke-width=".8"/><path d="M3.3 4.2L6 6.2l2.7-2" fill="none" stroke="#fff" stroke-width=".6"/></symbol>
    <symbol id="w-web" viewBox="0 0 12 12"><circle cx="6" cy="6" r="5.3" fill="none" stroke="#fff" stroke-width="1"/><rect x="3.4" y="3.8" width="5.2" height="3.6" rx=".4" fill="none" stroke="#fff" stroke-width=".8"/><path d="M5 8.4h2" stroke="#fff" stroke-width=".8"/></symbol>
  </defs>
</svg>

<!-- Envelope -->
<section class="piece envelope" aria-label="Envelope">
  <div class="photo" role="img" aria-label="Close-up photograph of a violin scroll and tuning pegs"></div>
  <div class="brand-name"><span class="brand-dot"></span>Lumora Music</div>
  <div class="contact-list">
    <div class="contact-row"><span class="contact-item"><svg class="icon"><use href="#i-pin"/></svg>Level 7, 41 Caddow Lane, Sydney, 2000</span></div>
    <div class="contact-row"><span class="contact-item"><svg class="icon"><use href="#i-phone"/></svg>0455&nbsp; 318&nbsp; 602</span><span class="contact-item"><svg class="icon"><use href="#i-mail"/></svg>contact@lumoramusicevents-demo.net</span></div>
    <div class="contact-row"><span class="contact-item"><svg class="icon"><use href="#i-mobile"/></svg>0455&nbsp; 318&nbsp; 602</span><span class="contact-item"><svg class="icon"><use href="#i-web"/></svg>www.lumoramusicevents-demo.net</span></div>
  </div>
  <div class="band"><div class="handle"><span class="handle-dot"></span>@lumoramusicevents</div></div>
</section>

<!-- Business card front -->
<section class="piece card-front" aria-label="Business card front">
  <div class="halo"></div>
  <div class="brand-name">Lumora Music</div>
</section>

<!-- Business card back -->
<section class="piece card-back" aria-label="Business card back">
  <div class="photo" role="img" aria-label="Faded photograph of a violin scroll"></div>
  <div class="holder">
    <div class="holder-name"><b>Clare</b> Yoshinaga</div>
    <div class="holder-role">violinist</div>
  </div>
  <div class="contact-list">
    <div class="contact-row"><span class="contact-item"><svg class="icon"><use href="#i-pin"/></svg>Level 7, 41 Caddow Lane, Sydney, 2000</span></div>
    <div class="contact-row"><span class="contact-item"><svg class="icon"><use href="#i-phone"/></svg>0455&nbsp; 318&nbsp; 602</span><span class="contact-item"><svg class="icon"><use href="#i-mail"/></svg>contact@lumoramusicevents-demo.net</span></div>
    <div class="contact-row"><span class="contact-item"><svg class="icon"><use href="#i-mobile"/></svg>0455&nbsp; 318&nbsp; 602</span><span class="contact-item"><svg class="icon"><use href="#i-web"/></svg>www.lumoramusicevents-demo.net</span></div>
  </div>
  <div class="handle"><span class="handle-dot"></span>@lumoramusicevents</div>
</section>

<!-- Letterhead -->
<section class="piece letterhead" aria-label="Letterhead">
  <svg class="header-band" viewBox="0 0 549 61" aria-hidden="true">
    <path d="M0 0H549V61H236Q224 61 222 48V30Q220 14 204 14H0Z" fill="var(--navy)"/>
  </svg>
  <div class="brand-name"><span class="brand-dot"></span>Lumora Music</div>
  <div class="contact-list">
    <div class="contact-row"><span class="contact-item"><svg class="icon"><use href="#w-pin"/></svg>Level 7, 41 Caddow Lane, Sydney, 2000</span></div>
    <div class="contact-row"><span class="contact-item"><svg class="icon"><use href="#w-phone"/></svg>0455&nbsp; 318&nbsp; 602</span><span class="contact-item"><svg class="icon"><use href="#w-mail"/></svg>contact@lumoramusicevents-demo.net</span></div>
    <div class="contact-row"><span class="contact-item"><svg class="icon"><use href="#w-mobile"/></svg>0455&nbsp; 318&nbsp; 602</span><span class="contact-item"><svg class="icon"><use href="#w-web"/></svg>www.lumoramusicevents-demo.net</span></div>
  </div>

  <div class="recipient">
    <div class="recipient-name">Clare Yoshinaga</div>
    <div>General Manager</div>
    <div>Address Line Goes Here</div>
  </div>
  <div class="letter-date">Date: 05-11-2018</div>

  <div class="letter-body">
    <p>Lorem ipsum dolor sit amet, consectetur adipiscing elit, sed do eiusmod tempor incididunt ut labore et dolore magna aliqua. Ut enim ad minim veniam, quis nostrud exercitation ullamco laboris nisi ut aliquip ex ea commodo consequat. Duis aute irure dolor in reprehenderit in voluptate velit esse cillum dolore eu fugiat nulla pariatur. Excepteur sint occaecat cupidatat non proident, sunt in culpa qui officia deserunt mollit anim id est laborum</p>
    <p>Sed ut perspiciatis unde omnis iste natus error sit voluptatem accusantium doloremque laudantium, totam rem aperiam, eaque ipsa quae ab illo inventore veritatis et quasi architecto beatae vitae dicta sunt explicabo. Nemo enim ipsam voluptatem quia voluptas sit aspernatur aut odit aut fugit, sed quia consequuntur magni dolores eos qui ratione voluptatem sequi nesciunt. Neque porro quisquam est, qui dolorem ipsum quia dolor sit amet, consectetur, adipisci velit, sed quia non numquam eius modi tempora incidunt ut labore et dolore magnam aliquam quaerat voluptatem. Ut enim ad minima veniam, quis nostrum exercitationem ullam corporis suscipit laboriosam, nisi ut aliquid ex ea commodi consequatur? Quis autem vel eum iure reprehenderit qui in ea voluptate velit esse quam nihil molestiae consequatur, vel illum qui dolorem eum fugiat quo voluptas nulla pariatur</p>
    <p>At vero eos et accusamus et iusto odio dignissimos ducimus qui blanditiis praesentium voluptatum deleniti atque corrupti quos dolores et quas molestias excepturi sint occaecati cupiditate non provident, similique sunt in culpa qui officia deserunt mollitia animi, id est laborum et dolorum fuga. Et harum quidem rerum facilis est et expedita distinctio. Nam libero tempore, cum soluta nobis est eligendi optio cumque nihil impedit quo minus id quod maxime placeat facere possimus, omnis voluptas assumenda est</p>
    <p>Lorem Ipsum is simply dummy text of the printing and typesetting industry</p>
  </div>

  <div class="sign-off">
    <div>Sincerely Your</div>
    <div class="signer">Maren Talbot</div>
    <div>Vice President</div>
  </div>

  <div class="footer-band">
    <div class="seg-left"></div>
    <div class="handle"><span class="handle-dot"></span>@lumoramusicevents</div>
    <div class="seg-right"></div>
  </div>
</section>

</body>
</html>
```